Outdoor Company Business Card design

We are an outdoor adventure company needing a business card. We sell outdoor adventures and clothing. Please use our logo in the business card. We are looking for something unique but delivers a clear message as to who we are. Please be creative

Target Market(s)

Outdoor adventures

Industry/Entity Type

Business

Contact Information for Business Card

Business name: TrailBrook If using the logo, no need to have a spot for the name
Owner / CEO: Owen Pardle
Website: TrailBrook.example
Facebook: Social.example/TrailBrook
Instagram: @pardle_owen
phone number: 555-384-7120
Email: Pardleteams@TrailBrook.example

Colors

Designer to choose colors to be used in the design.

Requirements
Must have
• The business card must include the details mentioned above. ie logo, my name, email, facebook, instagram, website, and phone number.
Should not have
• should not be cluttered or look messy

```html
<!DOCTYPE html>
<html lang="en">
<head>
<meta charset="utf-8">
<title>TrailBrook Business Card</title>
<link href="https://fonts.googleapis.com/css2?family=Montserrat:wght@500;600;700&family=Roboto:wght@400;500&display=swap" rel="stylesheet">
<style>
  :root {
    --page-bg: #1c1c1e;
    --card-bg: #2a2a2c;
    --card-edge: #333336;
    --brand-blue: #1f7fd6;
    --brand-orange: #f2602a;
    --text-light: #e6e6e6;
    --divider: #55555a;
  }
  * { margin: 0; padding: 0; box-sizing: border-box; }
  html, body { width: 903px; height: 1200px; overflow: hidden; }
  body {
    background: var(--page-bg);
    display: flex;
    flex-direction: column;
    align-items: center;
    justify-content: space-evenly;
    font-family: "Roboto", Arial, sans-serif;
  }
  .card {
    position: relative;
    width: 700px;
    height: 400px;
    background: var(--card-bg);
    border: 1px solid var(--card-edge);
    border-radius: 6px;
    overflow: hidden;
    box-shadow: 0 18px 40px rgba(0,0,0,0.45);
  }
  .brand-name {
    font-family: "Montserrat", sans-serif;
    font-weight: 700;
    color: var(--brand-blue);
    letter-spacing: 1px;
    text-transform: uppercase;
    white-space: nowrap;
  }
  .card-front { display: flex; align-items: center; justify-content: center; }
  .card-front .brand-name { font-size: 52px; }

  .card-back .brand-block {
    position: absolute;
    left: 40px;
    top: 178px;
  }
  .card-back .brand-name { font-size: 40px; }
  .card-back .divider {
    position: absolute;
    left: 352px;
    top: 92px;
    width: 1px;
    height: 170px;
    background: var(--divider);
  }
  .contact {
    position: absolute;
    left: 376px;
    top: 92px;
  }
  .contact .person-name {
    font-family: "Montserrat", sans-serif;
    font-weight: 600;
    font-size: 22px;
    color: var(--brand-blue);
    text-transform: uppercase;
    line-height: 1.1;
  }
  .contact .person-role {
    font-family: "Montserrat", sans-serif;
    font-weight: 600;
    font-size: 13px;
    color: var(--brand-orange);
    text-transform: uppercase;
    margin: 4px 0 12px;
  }
  .contact-list { list-style: none; }
  .contact-list li {
    display: flex;
    align-items: center;
    gap: 9px;
    font-size: 14px;
    color: var(--text-light);
    line-height: 1;
    margin-bottom: 8px;
    white-space: nowrap;
  }
  .icon {
    width: 14px; height: 14px;
    flex: none;
    display: block;
  }
  .bottom-band { position: absolute; left: 0; bottom: 0; width: 100%; height: 60px; }
</style>
</head>
<body>

  <section class="card card-front" aria-label="Card front">
    <span class="brand-name">TrailBrook</span>
  </section>

  <section class="card card-back" aria-label="Card back">
    <div class="brand-block"><span class="brand-name">TrailBrook</span></div>
    <div class="divider"></div>
    <div class="contact">
      <p class="person-name">Owen Pardle</p>
      <p class="person-role">Owner / CEO</p>
      <ul class="contact-list">
        <li>
          <svg class="icon" viewBox="0 0 14 14"><circle cx="7" cy="7" r="7" fill="#f2602a"/><path d="M4.3 3.6c.4-.3.9-.2 1.1.2l.6 1.2c.1.3 0 .6-.2.8l-.4.3c.4.9 1.1 1.6 2 2l.3-.4c.2-.2.5-.3.8-.2l1.2.6c.4.2.5.7.2 1.1-.5.7-1.3 1-2.1.7C5.9 9.3 4.7 8.1 4 6.2c-.3-.8 0-1.7.3-2.6z" fill="#fff"/></svg>
          555-384-7120
        </li>
        <li>
          <svg class="icon" viewBox="0 0 14 14"><circle cx="7" cy="7" r="7" fill="#f2602a"/><rect x="3.5" y="4.5" width="7" height="5" rx="0.6" fill="none" stroke="#fff" stroke-width="1"/><path d="M3.7 4.8 7 7.3l3.3-2.5" fill="none" stroke="#fff" stroke-width="1"/></svg>
          Pardleteams@TrailBrook.example
        </li>
        <li>
          <svg class="icon" viewBox="0 0 14 14"><circle cx="7" cy="7" r="7" fill="#f2602a"/><circle cx="7" cy="7" r="3.6" fill="none" stroke="#fff" stroke-width="0.9"/><path d="M3.4 7h7.2M7 3.4c-1.6 2.2-1.6 5 0 7.2M7 3.4c1.6 2.2 1.6 5 0 7.2" fill="none" stroke="#fff" stroke-width="0.8"/></svg>
          www.TrailBrook.example
        </li>
        <li>
          <svg class="icon" viewBox="0 0 14 14"><rect width="14" height="14" rx="2" fill="#1f7fd6"/></svg>
          Social.example/TrailBrook
        </li>
        <li>
          <svg class="icon" viewBox="0 0 14 14"><rect width="14" height="14" rx="2" fill="#1f7fd6"/></svg>
          @pardle_owen
        </li>
      </ul>
    </div>
    <svg class="bottom-band" viewBox="0 0 700 60" preserveAspectRatio="none" aria-hidden="true">
      <polygon points="0,52 330,52 322,60 0,60" fill="var(--brand-orange)"/>
      <polygon points="340,42 700,42 700,60 330,60" fill="var(--brand-blue)"/>
    </svg>
  </section>

</body>
</html>
```